signage for halvin rx (pharmacy and surgical supply)

we created logo for halvin rx , we want to see if it could be modified , also we need signage. please review the attachment

```html
<!DOCTYPE html>
<html lang="en">
<head>
<meta charset="utf-8">
<title>Halvin Rx – Storefront Sign</title>
<link rel="stylesheet" href="https://fonts.googleapis.com/css2?family=Montserrat:wght@600&family=Yellowtail&family=Playfair+Display:wght@400;600&family=Roboto+Condensed:wght@800;900&display=swap">
<style>
  :root {
    --bg: #ffffff;
    --frame: #3a1d33;
    --panel: #d6cbbb;
    --edge: #f4efe8;
    --rx-name: #1f7fc1;
    --juice: #6aa33a;
    --nails: #c05073;
    --pharmacy: #e0242a;
  }
  html, body {
    margin: 0;
    width: 1200px;
    height: 854px;
    overflow: hidden;
    background: var(--bg);
  }
  .canvas {
    position: relative;
    width: 1200px;
    height: 854px;
  }
  .sign {
    position: absolute;
    left: 183px;
    top: 154px;
    width: 695px;
    height: 455px;
    transform: scale(1.2);
    transform-origin: top left;
  }
  .sign-shape {
    position: absolute;
    inset: 0;
  }
  .tenant {
    position: absolute;
    line-height: 1;
    white-space: nowrap;
  }
  .tenant--rx {
    left: 45px;
    top: 157px;
    width: 295px;
    text-align: center;
    font-family: "Montserrat", sans-serif;
    font-weight: 600;
    font-size: 46px;
    color: var(--rx-name);
  }
  .tenant--juice {
    left: 350px;
    top: 118px;
    width: 300px;
    text-align: center;
    font-family: "Yellowtail", cursive;
    font-size: 72px;
    color: var(--juice);
  }
  .tenant--nails {
    left: 45px;
    top: 250px;
    width: 295px;
    text-align: center;
    color: var(--nails);
    font-family: "Playfair Display", serif;
  }
  .tenant--nails .line-top {
    display: block;
    font-size: 34px;
    font-weight: 400;
  }
  .tenant--nails .line-main {
    display: block;
    font-size: 44px;
    font-weight: 600;
    margin-top: 2px;
  }
  .tenant--pharmacy {
    left: 362px;
    top: 252px;
    width: 280px;
    text-align: left;
    color: var(--pharmacy);
    font-family: "Roboto Condensed", sans-serif;
  }
  .tenant--pharmacy .line-main {
    display: block;
    font-size: 58px;
    font-weight: 900;
    letter-spacing: 0.5px;
  }
  .tenant--pharmacy .line-sub {
    display: block;
    font-size: 27px;
    font-weight: 800;
    letter-spacing: 1.2px;
    margin-top: -1px;
  }
</style>
</head>
<body>
<main class="canvas">
  <section class="sign" aria-label="Storefront tenant sign">
    <svg class="sign-shape" viewBox="0 0 695 455" width="695" height="455" aria-hidden="true">
      <path fill="var(--frame)" d="M334,4 Q347,0 360,4 L650,90 Q695,104 695,150 L695,330 Q695,362 665,373 L360,452 Q347,456 334,452 L30,373 Q0,362 0,330 L0,150 Q0,104 45,90 Z"/>
      <g transform="translate(15,15) scale(0.9568,0.934)">
        <path fill="var(--panel)" stroke="var(--edge)" stroke-width="3" d="M334,4 Q347,0 360,4 L650,90 Q695,104 695,150 L695,330 Q695,362 665,373 L360,452 Q347,456 334,452 L30,373 Q0,362 0,330 L0,150 Q0,104 45,90 Z"/>
      </g>
    </svg>

    <div class="tenant tenant--rx">HALVIN RX</div>
    <div class="tenant tenant--juice">Juice Bar</div>
    <div class="tenant tenant--nails">
      <span class="line-top">Rose Petal</span>
      <span class="line-main">NAILS &amp; SPA</span>
    </div>
    <div class="tenant tenant--pharmacy">
      <span class="line-main">PHARMACY</span>
      <span class="line-sub">&amp; SURGICAL SUPPLY</span>
    </div>
  </section>
</main>
</body>
</html>
```